New Company Introduction

We have launched a new business channel and need an online 'brochure' that we can use to announce us. Short, no more than 5 pages, clean, simple and changeable as we develop. See our new website for direction www.skyvellcare-example.com the introduction is to be issued to insurance companies, government departments and private clinics

Industry/Entity Type

Government

Font styles to use
Sans Serif

```html
<!DOCTYPE html>
<html lang="en">
<head>
<meta charset="utf-8">
<title>Skyvell Air Care – Introduction Brochure</title>
<link rel="stylesheet" href="https://fonts.googleapis.com/css2?family=Roboto+Condensed:wght@300;400&family=Lato:wght@400;700&display=swap">
<style>
  :root {
    --page-bg: #e9ebef;
    --paper: #ffffff;
    --blue: #1f5fd6;
    --blue-deep: #0f3fae;
    --blue-light: #5d93ea;
    --blue-pale: #bcd2f5;
    --ink: #222a36;
    --ink-soft: #2c3f8c;
  }
  * { margin: 0; padding: 0; box-sizing: border-box; }
  html, body { width: 1200px; height: 875px; overflow: hidden; }
  body { background: var(--page-bg); position: relative; font-family: "Lato", Arial, sans-serif; }

  .brochure-spread {
    position: absolute; left: 48px; top: 241px;
    width: 1104px; height: 392px;
    background: var(--paper);
    box-shadow: 0 6px 18px rgba(0,0,0,0.18);
    overflow: hidden;
  }
  .spread-shapes { position: absolute; inset: 0; width: 100%; height: 100%; }

  .back-cover__website {
    position: absolute; left: 58px; top: 208px;
    font-family: "Roboto Condensed", Arial, sans-serif; font-weight: 400;
    font-size: 24px; line-height: 30px; color: var(--paper);
    white-space: nowrap;
  }
  .back-cover__quote {
    position: absolute; left: 26px; top: 268px; width: 405px;
    font-size: 14.5px; line-height: 1.35; color: var(--ink);
  }
  .back-cover__quote .mark { font-size: 20px; line-height: 0; vertical-align: -3px; }
  .back-cover__quote .line-end { display: block; text-align: right; }
  .back-cover__contact {
    position: absolute; left: 140px; top: 330px; width: 200px;
    list-style: none; text-align: center;
    font-size: 8.5px; line-height: 1.35; color: var(--ink-soft);
  }
  .back-cover__contact li { display: flex; justify-content: center; align-items: flex-start; gap: 4px; }
  .back-cover__contact svg { width: 8px; height: 8px; margin-top: 1px; flex: none; fill: var(--ink); }

  .front-cover__brand {
    position: absolute; left: 576px; top: 332px;
    display: flex; align-items: center; gap: 10px;
    font-family: "Roboto Condensed", Arial, sans-serif; font-weight: 400;
    font-size: 33px; color: var(--paper); white-space: nowrap;
  }
  .front-cover__brand-dot {
    position: absolute; left: 0; top: -64px;
    width: 50px; height: 50px; border-radius: 50%;
    border: 2px solid var(--paper);
  }
</style>
</head>
<body>
  <main class="brochure-spread">
    <svg class="spread-shapes" viewBox="0 0 920 327" preserveAspectRatio="none">
      <defs>
        <linearGradient id="photo-tones" x1="0" y1="0" x2="1" y2="1">
          <stop offset="0" stop-color="#e8e6e4"/>
          <stop offset="0.45" stop-color="#d8dbe2"/>
          <stop offset="0.7" stop-color="#a9b6d4"/>
          <stop offset="1" stop-color="#f1f0ee"/>
        </linearGradient>
        <linearGradient id="blue-sweep" x1="0" y1="0" x2="1" y2="0">
          <stop offset="0" stop-color="#1a55cf"/>
          <stop offset="1" stop-color="#2f73e6"/>
        </linearGradient>
      </defs>

      <rect x="460" y="0" width="460" height="327" fill="url(#photo-tones)" role="img"
            aria-label="Photograph: two doctors in white coats checking on a smiling senior patient in a clinic"/>

      <circle cx="72" cy="60" r="38" fill="#eef0f4"/>
      <rect x="0" y="160" width="380" height="53" fill="var(--blue)"/>
      <polygon points="0,262 0,327 62,327" fill="var(--blue)"/>

      <polygon points="180,0 350,0 480,150 460,327 455,327" fill="url(#blue-sweep)"/>
      <polygon points="350,0 395,0 560,200 480,150" fill="var(--blue-light)" opacity="0.75"/>
      <polygon points="395,0 430,0 600,215 560,200" fill="var(--blue-pale)" opacity="0.7"/>
      <polygon points="430,0 450,0 640,228 600,215" fill="#ffffff" opacity="0.55"/>

      <polygon points="455,327 480,150 560,215 920,318 920,327" fill="url(#blue-sweep)"/>
      <polygon points="560,215 640,228 920,306 920,318" fill="var(--blue-pale)" opacity="0.8"/>
      <polygon points="545,170 590,160 590,215 560,215" fill="var(--blue-deep)" opacity="0.6"/>

      <polygon points="855,0 920,0 920,70" fill="var(--blue)"/>
    </svg>

    <p class="back-cover__website">www.skyvellcare-example.com</p>

    <blockquote class="back-cover__quote">
      <span class="mark">“</span>We could not have asked for a better service. Once again,
      <span class="line-end">thank you!<span class="mark">”</span></span>
    </blockquote>

    <ul class="back-cover__contact">
      <li>
        <svg viewBox="0 0 10 10"><path d="M5 1 1 5h1.2v4h2.3V6.5h1V9h2.3V5H9z"/></svg>
        <span>Northwind Aviation Ltd, Elmbridge, Sampleshire<br>United Kingdom, ZZ1 0AA</span>
      </li>
      <li>
        <svg viewBox="0 0 10 10"><path d="M0 2h10v6H0z M0 2l5 3.5L10 2" /></svg>
        <span>operations@skyvell-example.com</span>
      </li>
      <li>
        <svg viewBox="0 0 10 10"><path d="M2 0.5 3.8 2.6 3 4c.7 1.3 1.7 2.3 3 3l1.4-.8L9.5 8 8.2 9.5C4 9 1 6 .5 1.8z"/></svg>
        <span>+44 (0)200 000 0000</span>
      </li>
    </ul>

    <div class="front-cover__brand">
      <span class="front-cover__brand-dot"></span>
      <span class="front-cover__brand-name">Skyvell Air Care</span>
    </div>
  </main>
</body>
</html>
```